Illustrations, Icons and placement

Wire frame will describe it best, https://plindra.com/diagrams/kVbrTeLoqzMeeyfp

With the direction of my mockups I am going to require illustrations with similarity to the mock up. I need icons for my slider and of course beautiful slides. It is not necessary to design the webpage, I know where I want to go with this, I really just need strong illustrations.

This is the first serious design submitted. I appreciate the obvious hard work. To be honest, this system is not great for designers to know exactly what I want but finding a designer that can put in the effort to get there is the trick.

I have locked in the front page design to something that is very accurately portrayed in the mockup. The reason why is the illustration I will using. Currently My mock up shows flower on a hill, i replace with an launchbox illustration, see uploaded file to review... Also, colors are definatly what I am looking for but this ok for now. Your design is good..
Updates

Project Deadline Extended
Reason: my choice needs more time to finish the design before we begin

Target Market(s)

SaaS Consumer

Industry/Entity Type

Work

Requirements
Must have
• Display features in a nice slider like

http://www.brivotech.com/hartfield/index.php

room in header for new illustration, see attachment
Should not have
• Traditional out dated designs that look like templates

```html
<!DOCTYPE html>
<html lang="en">
<head>
<meta charset="utf-8">
<title>Hosting</title>
<link rel="stylesheet" href="https://fonts.googleapis.com/css2?family=Tinos:wght@400;700&family=PT+Sans:wght@400;700&display=swap">
<style>
:root{
  --bg:#0a0a09;
  --bg-edge:#1a1815;
  --nav-label:#8d7157;
  --active:#52c262;
  --icon:#0c0c0b;
  --icon-glow:rgba(150,90,30,.45);
  --heading-green:#4f8b5c;
  --body-brown:#8a6b55;
  --link-orange:#d79a2b;
  --panel:#020202;
  --tab-top:#4ccb58;
  --tab-bottom:#33a043;
  --tab-text:#e8f2e6;
  --title-gold:#8c6a2c;
  --intro:#cfd8d6;
  --list:#9a8b79;
  --price-top:#f0e35c;
  --price-bottom:#fbaa2e;
  --price-ink:#4a3a22;
  --chart-top:#eef0c4;
  --chart-bottom:#e0e4a8;
}
*{margin:0;padding:0;box-sizing:border-box}
html,body{width:1200px;height:901px;overflow:hidden}
body{
  position:relative;
  background:radial-gradient(ellipse at 50% 45%,#0c0c0b 55%,var(--bg-edge) 100%),var(--bg);
  font-family:"PT Sans",sans-serif;
}
.nav{
  position:absolute;left:108px;top:0;width:957px;height:136px;
  background:linear-gradient(#2a1a0c 0%,#140e08 45%,#0b0a09 100%);
}
.nav-item{position:absolute;top:0;width:140px;text-align:center;
  font-family:"Tinos",serif;font-weight:700;font-size:14px;line-height:18px;color:var(--nav-label)}
.nav-item svg{display:block;margin:0 auto;filter:drop-shadow(0 0 5px var(--icon-glow))}
.nav-item span{position:absolute;left:0;right:0}
.nav-item.is-active{color:var(--active)}
.nav-item.is-active svg{filter:none}

.screen-art{position:absolute;left:108px;top:209px;width:390px;height:313px;
  background:linear-gradient(135deg,#3a3a3a 0%,#1d1d1d 50%,#101010 70%,#bdbdbd 100%);
  border-radius:8px}
.divider{position:absolute;left:542px;top:185px;width:2px;height:356px;
  background:linear-gradient(transparent,#8a6a4a 50%,transparent)}

.feature{position:absolute;width:214px}
.feature h3{font-family:"Tinos",serif;font-weight:700;font-size:19px;color:var(--heading-green);letter-spacing:.7px;line-height:24px;white-space:nowrap}
.feature p{margin-top:10px;font-size:15.6px;line-height:23px;color:var(--body-brown)}
.feature a{display:block;text-align:right;font-family:"Tinos",serif;font-size:15px;color:var(--link-orange);text-decoration:none;line-height:20px}

.plans{position:absolute;left:108px;top:568px;width:957px;height:360px;border-radius:14px;
  background:linear-gradient(var(--panel) 60%,#1e140b 100%)}
.tab{position:absolute;top:18px;width:60px;height:340px;border-radius:3px;
  background:linear-gradient(var(--tab-top),var(--tab-bottom))}
.tab span{position:absolute;left:50%;top:147px;transform:translate(-50%,-50%) rotate(-90deg);
  font-weight:700;font-size:21px;color:var(--tab-text);white-space:nowrap;letter-spacing:.5px}
.plan-title{position:absolute;left:185px;top:26px;font-family:"Tinos",serif;font-weight:400;font-size:24px;color:var(--title-gold)}
.plan-intro{position:absolute;left:192px;top:80px;width:276px;font-family:"Tinos",serif;font-size:17px;line-height:21px;color:var(--intro)}
.plan-list{position:absolute;left:245px;top:177px;list-style:none;font-family:"Tinos",serif;font-size:17px;line-height:21px;color:var(--list)}
.plan-list li::before{content:"•";font-size:13px;margin-right:8px;vertical-align:2px}
.price{position:absolute;left:513px;top:61px;width:188px;height:164px;border-radius:9px;
  background:linear-gradient(var(--price-top),var(--price-bottom));text-align:center;color:var(--price-ink);
  box-shadow:0 0 0 1px #c98a20 inset}
.price-amount{font-family:"Tinos",serif;font-size:50px;line-height:50px;margin-top:20px}
.price-amount sup{font-size:24px;vertical-align:20px;margin-right:2px}
.price-term{font-family:"Tinos",serif;font-size:19px;line-height:22px}
.price-cta{font-size:13px;margin-top:5px;color:#3a2e1c}
.compare{position:absolute;left:513px;top:231px;width:188px;height:80px;border-radius:9px;
  background:linear-gradient(var(--chart-top),var(--chart-bottom));text-align:center;
  font-family:"Tinos",serif;font-size:20px;line-height:25px;color:#2e2e28;padding-top:16px}
</style>
</head>
<body>
<nav class="nav">
  <div class="nav-item" style="left:56px">
    <svg width="120" height="76" viewBox="0 0 120 76"><g fill="var(--icon)"><circle cx="36" cy="18" r="13"/><path d="M14 66q0-30 22-30t22 30z"/><circle cx="82" cy="18" r="13"/><path d="M60 66q0-30 22-30t22 30z"/></g></svg>
    <span style="top:89px">Collaborate</span>
  </div>
  <div class="nav-item" style="left:200px">
    <svg width="120" height="76" viewBox="0 0 120 76"><g fill="var(--icon)"><circle cx="52" cy="18" r="13"/><path d="M30 68q0-32 22-32t22 32z"/></g><circle cx="86" cy="26" r="8" fill="none" stroke="var(--icon)" stroke-width="3"/><path d="M92 32l9 9" stroke="var(--icon)" stroke-width="4"/></svg>
    <span style="top:81px">Find<br>Professionals</span>
  </div>
  <div class="nav-item" style="left:336px">
    <svg width="120" height="76" viewBox="0 0 120 76"><g fill="var(--icon)"><ellipse cx="58" cy="12" rx="16" ry="5"/><path d="M42 12v42q16 8 32 0V12z"/><ellipse cx="72" cy="60" rx="12" ry="4"/></g></svg>
    <span style="top:81px">Theme<br>Builder</span>
  </div>
  <div class="nav-item is-active" style="left:478px">
    <svg width="120" height="76" viewBox="0 0 120 76"><g fill="#2f8a44" stroke="#0a0a09" stroke-width="2"><ellipse cx="60" cy="54" rx="39" ry="10"/><rect x="21" y="44" width="78" height="10" stroke="none"/><ellipse cx="60" cy="44" rx="39" ry="10"/><rect x="21" y="28" width="78" height="14" stroke="none"/><ellipse cx="60" cy="29" rx="39" ry="10"/><rect x="21" y="12" width="78" height="16" stroke="none"/><ellipse cx="60" cy="12" rx="39" ry="9"/></g></svg>
    <span style="top:90px">Hosting</span>
  </div>
  <div class="nav-item" style="left:619px">
    <svg width="120" height="76" viewBox="0 0 120 76"><g stroke="var(--icon)" stroke-width="9" stroke-linecap="round"><path d="M40 10l40 52"/><path d="M82 12L40 60"/></g><circle cx="84" cy="10" r="9" fill="var(--icon)"/></svg>
    <span style="top:81px">Developer<br>Tools</span>
  </div>
  <div class="nav-item" style="left:758px">
    <svg width="120" height="76" viewBox="0 0 120 76"><g stroke="var(--icon)" stroke-width="3"><path d="M60 6v62M32 36h56M40 16l40 40M80 16L40 56"/></g><circle cx="60" cy="36" r="7" fill="var(--icon)"/></svg>
    <span style="top:92px">Distributions</span>
  </div>
</nav>

<div class="screen-art" role="img" aria-label="Illustration of a desktop computer monitor"></div>
<div class="divider"></div>

<section class="feature" style="left:585px;top:206px">
  <h3>AUTO BACKUP</h3>
  <p>Dictumst purus augue, a amet, lundium augue, cras, etiam dipice parturient augue, tempor cum pellentesque. Lectus</p>
  <a href="#">read more...</a>
</section>
<section class="feature" style="left:843px;top:206px">
  <h3>EASY UPLOADING</h3>
  <p>Sed est sed pulvinar montes arcu nec magna, turpis purus ridiculus. Integer lacus egestas.</p>
  <a href="#" style="margin-top:23px">read more...</a>
</section>
<section class="feature" style="left:585px;top:382px">
  <h3>SQL TABLEDESK</h3>
  <p>Dictumst purus augue, a amet, lundium augue, cras, etiam adipiscing parturient augue, tempor cum pellentesque.</p>
  <a href="#">read more...</a>
</section>
<section class="feature" style="left:840px;top:382px">
  <h3>EASY DEPLOYEMENT</h3>
  <p>Dictumst purus augue, a amet, lundium augue, cras, etiam adipiscing parturient augue, tempor cum pellentesque.</p>
  <a href="#">read more...</a>
</section>

<section class="plans">
  <div class="tab" style="left:34px"><span>Free</span></div>
  <div class="tab" style="left:99px"><span>Basic</span></div>
  <h2 class="plan-title">Basic Hosting</h2>
  <p class="plan-intro">With basic you get all the great options that come in the free package, along with a myriad of other great features:</p>
  <ul class="plan-list">
    <li>500GB bandwidth</li><li>5GB storage</li><li>Site duplication</li><li>Import</li><li>Backup</li><li>Modules/Themes</li><li>Updates</li>
  </ul>
  <div class="price">
    <div class="price-amount"><sup>$</sup>11</div>
    <div class="price-term">MONTHLY</div>
    <div class="price-cta">Sign Up Now</div>
  </div>
  <div class="compare">See the price<br>comparison chart</div>
  <div class="tab" style="left:738px"><span>Pro</span></div>
  <div class="tab" style="left:803px"><span>Advanced</span></div>
  <div class="tab" style="left:867px"><span>Business</span></div>
</section>
</body>
</html>
```